Outdoor cooking competition needs 10yr celebration poster

We are a fundraising event held every year in a tiny outback town in australia. the cooking competition is a 'camp oven' themed competition. people are required to cook in the ground in coals with a camp oven (dutch oven).
the event is celebrating ten years and needs a new flashy poster to let people know.

the event raises much needed funds for "the Sunward Air Medic" a a donation funded scheme which flys doctors and patients to and from remote australia.

The EMBER DUST FEAST is held annually in the tiny town of Blinman in the northern Flinders Ranges. The main street of the town, camp ground, and surrounding area have been landscaped to suit the competitions purpose. A giant ‘creek bed’ kitchen is created with tones of rocks and gravel transforming the street and adjacent hill side. The picturesque and historic Quarrow Hotel with its verandahs and characteristic front bar, will form a focus, the remaining street precinct will be the venue for exhibitions, wine tasting, food outlets, trade displays, demonstrations and live music.

Payment now GARAUNTEED!

• Must display our logo
dates and venues
10 year celebration
room to add sponsorship logos

```html
<!DOCTYPE html>
<html lang="en">
<head>
<meta charset="utf-8">
<title>Ember Dust Feast – Camp Oven Cook Off</title>
<link rel="stylesheet" href="https://fonts.googleapis.com/css2?family=Inter:wght@300;800&display=swap">
<style>
  :root {
    --bg: #f49a31;
    --red: #a7291b;
    --green: #4e9a4f;
    --white: #ffffff;
    --cream: #f8f1b2;
    --ink: #111111;
    --rise: -28deg;
    --fall: 57deg;
  }
  html, body {
    margin: 0;
    padding: 0;
    width: 849px;
    height: 1200px;
    overflow: hidden;
    background: var(--bg);
  }
  .poster {
    position: relative;
    width: 849px;
    height: 1200px;
    background: var(--bg);
    overflow: hidden;
    font-family: "Inter", "Helvetica Neue", Arial, sans-serif;
  }
  /* each line is anchored at the left end of its baseline */
  .line {
    position: absolute;
    margin: 0;
    white-space: nowrap;
    line-height: 1;
    letter-spacing: -0.03em;
    left: var(--x);
    top: calc(var(--y) - 0.864em);
    transform-origin: 0 0.864em;
    transform: rotate(var(--angle));
  }
  .rise { --angle: var(--rise); }
  .fall { --angle: var(--fall); }
  .light { font-weight: 300; }
  .bold { font-weight: 800; }
  .red { color: var(--red); }
  .green { color: var(--green); }
  .white { color: var(--white); }
  .cream { color: var(--cream); }

  .days        { --x: 196px; --y: 85px;  font-size: 78px; letter-spacing: -0.02em; }
  .month       { --x: 92px;  --y: 55px;  font-size: 72px; letter-spacing: 0.01em; }
  .dates       { --x: 28px;  --y: 128px; font-size: 80px; letter-spacing: -0.02em; }

  .venue-name  { --x: 432px; --y: 326px; font-size: 70px; }
  .venue-type  { --x: 470px; --y: 392px; font-size: 84px; }
  .title-camp  { --x: 50px;  --y: 765px; font-size: 150px; }
  .title-oven  { --x: 465px; --y: 545px; font-size: 145px; }
  .title-cook  { --x: 123px; --y: 880px; font-size: 165px; }
  .anniversary { --x: 155px; --y: 948px; font-size: 39px; }
  .prize       { --x: 185px; --y: 990px; font-size: 36px; }

  .event-mark {
    position: absolute;
    left: 365px;
    top: 112px;
    width: 140px;
    margin: 0;
    transform: rotate(-8deg);
    color: var(--ink);
    font-weight: 800;
    font-size: 30px;
    line-height: 34px;
    letter-spacing: -0.02em;
    text-align: center;
  }
</style>
</head>
<body>
<main class="poster">
  <p class="event-mark">EMBER<br>DUST<br>FEAST</p>

  <p class="line fall days"><span class="bold green">SAT</span><span class="light cream">&amp;</span><span class="bold green">SUN</span></p>
  <p class="line fall month light cream">SEPTEMBER</p>
  <p class="line fall dates"><span class="bold green">29</span><span class="light green">&amp;</span><span class="bold green">30</span><span class="light green">2012</span></p>

  <p class="line rise venue-name light white">QUARROW</p>
  <p class="line rise venue-type bold red">HOTEL</p>

  <h1 class="line rise title-camp bold red">CAMP</h1>
  <p class="line rise title-oven light green">OVEN</p>
  <h2 class="line rise title-cook"><span class="light white">COOK</span><span class="bold cream">OFF</span></h2>

  <p class="line rise anniversary"><span class="bold red">10</span><span class="light red">YEAR</span><span class="bold red">CELEBRATION</span></p>
  <p class="line rise prize"><span class="light cream">$5000</span><span class="bold cream">IN</span><span class="light cream">PRIZE</span><span class="bold cream">MONEY</span></p>
</main>
</body>
</html>
```